New Business Card Design Project

Hi there

Could you please make a design that is soft and appealing to people who would purchase gemstones, buy healing jewellery, seek counselling, may seek energy healing and/or learn English. Essentially I'm looking for something with a soft human design. Please incorporate the logo and select font that can be easily read and softer images in the background - but not too busy. I would like it double sided as well.

Optional: Elements could include gemstones, feathers, plants and images that are happy and calming.

Target Market(s)

People into alternative health, those from non-English speaking backgrounds, businesses

Contact Information for Business Card

Lena Whitford
Mobile: 0418 265 093, Friendloop and Snapfolio Logos,
ABN: 61 472 185 034 (Australian Business Number - small at the bottom)

Requirements
Must have
• My project must have:
- Meadow Thread logo
- Symbols that represent the 4 main services: 1. Gemstones/jewellery, 2. counselling, 3. meditation/energy healing, 4. education
Nice to have
• Clear and easy to read.

```html
<!DOCTYPE html>
<html lang="en">
<head>
<meta charset="utf-8">
<title>Meadow Thread — Business Card</title>
<link href="https://fonts.googleapis.com/css2?family=Arimo:wght@400;700&display=swap" rel="stylesheet">
<style>
  :root {
    --backdrop: #f1f3f3;
    --card-white: #fbfcfc;
    --teal: #14ad9f;
    --teal-deep: #0fa597;
    --ink-light: #ffffff;
    --shadow: rgba(40, 60, 65, 0.18);
  }
  * { box-sizing: border-box; margin: 0; padding: 0; }
  html, body {
    width: 1200px; height: 800px; overflow: hidden;
    background: var(--backdrop);
    font-family: "Arimo", Arial, sans-serif;
  }
  .canvas { position: relative; width: 1200px; height: 800px; }

  .card {
    position: absolute; top: 192px; width: 237px; height: 414px;
    background: var(--card-white);
    box-shadow: 0 2px 8px var(--shadow);
  }
  .card--front { left: 314px; }
  .card--back { left: 651px; }

  /* Front side */
  .brand-mark {
    position: absolute; left: 50%; top: 52px; transform: translateX(-50%);
    width: 34px; height: 34px; border-radius: 50%;
    border: 2px solid var(--teal);
  }
  .brand-name {
    position: absolute; left: 0; right: 0; top: 96px;
    text-align: center; color: var(--teal);
    font-weight: 700; font-size: 17px; letter-spacing: 1px;
  }
  .services {
    position: absolute; left: 16px; right: 16px; top: 196px;
    display: flex; justify-content: space-between;
  }
  .service-hex { width: 48px; height: 48px; display: block; }
  .service-hex .hex { fill: var(--teal); }
  .service-hex .glyph {
    fill: none; stroke: var(--ink-light); stroke-width: 1.4;
    stroke-linejoin: round; stroke-linecap: round;
  }

  .name-band {
    position: absolute; left: 0; right: 0; top: 277px;
    display: flex; align-items: center; gap: 8px;
  }
  .name-band__bar { height: 9px; background: var(--teal); flex: 1; }
  .name-band__text {
    color: var(--teal); font-weight: 700; font-size: 13px; letter-spacing: 1.3px;
  }

  .contact-phone {
    position: absolute; left: 0; right: 0; top: 317px;
    display: flex; justify-content: center; align-items: center; gap: 8px;
    color: var(--teal); font-weight: 700; font-size: 13px; letter-spacing: 1.4px;
  }
  .contact-phone svg { width: 10px; height: 15px; }

  .socials {
    position: absolute; left: 0; right: 0; top: 356px;
    display: flex; justify-content: center; gap: 14px;
  }
  .social {
    display: flex; align-items: center; gap: 4px;
    color: var(--teal); font-weight: 700; font-size: 10px;
  }
  .social__square { width: 10px; height: 10px; background: var(--teal); }

  .abn {
    position: absolute; left: 0; right: 0; top: 391px;
    text-align: center; color: var(--teal);
    font-size: 8px; letter-spacing: 0.8px;
  }

  /* Back side */
  .back-panel {
    position: absolute; left: 16px; top: 16px; right: 16px; bottom: 24px;
    background: linear-gradient(135deg, var(--teal) 0%, var(--teal-deep) 100%);
  }
  .back-panel .brand-mark {
    top: 115px; width: 58px; height: 58px; border-color: var(--ink-light);
  }
  .back-panel .brand-name {
    top: 194px; color: var(--ink-light); font-size: 18px;
  }
</style>
</head>
<body>
<main class="canvas">
  <section class="card card--front" aria-label="Card front">
    <div class="brand-mark"></div>
    <div class="brand-name">Meadow Thread</div>

    <div class="services">
      <svg class="service-hex" viewBox="0 0 48 48" role="img" aria-label="Gemstones and jewellery">
        <polygon class="hex" points="12,2 36,2 48,24 36,46 12,46 0,24"/>
        <g class="glyph">
          <polygon points="17,18 31,18 36,23 24,36 12,23"/>
          <polyline points="12,23 36,23"/>
          <polyline points="20,18 18,23 24,36 30,23 28,18"/>
        </g>
      </svg>
      <svg class="service-hex" viewBox="0 0 48 48" role="img" aria-label="Counselling">
        <g class="glyph">
        </g>
        <polygon class="hex" points="12,2 36,2 48,24 36,46 12,46 0,24"/>
        <g class="glyph">
          <path d="M12 15 h14 a2 2 0 0 1 2 2 v7 a2 2 0 0 1 -2 2 h-9 l-4 3 v-3 h-1 a2 2 0 0 1 -2 -2 v-7 a2 2 0 0 1 2 -2 z"/>
          <path d="M31 21 h4 a2 2 0 0 1 2 2 v7 a2 2 0 0 1 -2 2 h-1 v3 l-4 -3 h-7 a2 2 0 0 1 -2 -2 v-2"/>
        </g>
      </svg>
      <svg class="service-hex" viewBox="0 0 48 48" role="img" aria-label="Meditation and energy healing">
        <polygon class="hex" points="12,2 36,2 48,24 36,46 12,46 0,24"/>
        <g class="glyph">
          <path d="M24 13 c5 5 5 13 0 19 c-5 -6 -5 -14 0 -19 z"/>
          <path d="M24 32 c-4 -1 -9 -4 -10 -11 c5 0 9 3 10 7"/>
          <path d="M24 32 c4 -1 9 -4 10 -11 c-5 0 -9 3 -10 7"/>
          <path d="M14 35 h20"/>
        </g>
      </svg>
      <svg class="service-hex" viewBox="0 0 48 48" role="img" aria-label="Education">
        <polygon class="hex" points="12,2 36,2 48,24 36,46 12,46 0,24"/>
        <g class="glyph">
          <polygon points="24,15 38,21 24,27 10,21"/>
          <path d="M16 24 v6 c4 3 12 3 16 0 v-6"/>
          <path d="M36 22 v8"/>
          <circle cx="36" cy="31.5" r="1.2"/>
        </g>
      </svg>
    </div>

    <div class="name-band">
      <span class="name-band__bar"></span>
      <span class="name-band__text">Lena Whitford</span>
      <span class="name-band__bar"></span>
    </div>

    <div class="contact-phone">
      <svg viewBox="0 0 10 15" aria-hidden="true"><rect x="0.8" y="0.8" width="8.4" height="13.4" rx="1.5" fill="none" stroke="currentColor" stroke-width="1.4"/><rect x="3.5" y="11.3" width="3" height="1.2" fill="currentColor"/></svg>
      <span>0418 265 093</span>
    </div>

    <div class="socials">
      <span class="social"><span class="social__square"></span>Friendloop</span>
      <span class="social"><span class="social__square"></span>Snapfolio</span>
    </div>

    <div class="abn">ABN 61 472 185 034</div>
  </section>

  <section class="card card--back" aria-label="Card back">
    <div class="back-panel">
      <div class="brand-mark"></div>
      <div class="brand-name">Meadow Thread</div>
    </div>
  </section>
</main>
</body>
</html>
```